Presentation Folder Cover For Plumbing Company

We need a presentation folder cover (FRONT AND BACK) for our plumbing business.

We specialise in plumbing, hot water, electrical and pipe relining.

This will be sent to clients and the contents pages will outline all of our company details and information.

The target market for this cover is Strata / Property Managers who look after unit buildings.

Target Market(s)

Strata & Property Managers. The higher end of the property market.

Industry/Entity Type

Plumbing

Font styles to use
Sans Serif

Colors
ec1f27
0355a3
ffffff
474747
c9c9c9

Requirements
Must have
• A4 Paper Size
• Inviting to clients to open the document and read on.
Nice to have
• Sleek, Professional and Stands Out.
Should not have
• Dark Background. Needs to be fresh and bright.

```html
<!DOCTYPE html>
<html lang="en">
<head>
<meta charset="utf-8">
<title>Crest Contracting – Presentation Folder Cover</title>
<link href="https://fonts.googleapis.com/css2?family=Montserrat:wght@500;600;800&display=swap" rel="stylesheet">
<style>
  :root {
    --red: #ec1f27;
    --navy: #0355a3;
    --white: #ffffff;
    --ink: #474747;
    --silver: #c9c9c9;
    --sky-deep: #14b2ea;
    --sky-mid: #6fd0f3;
    --sky-pale: #e6f7fe;
    --stage: #e4e5e7;
  }
  * { box-sizing: border-box; margin: 0; padding: 0; }
  html, body { width: 1200px; height: 1200px; overflow: hidden; background: var(--stage); }
  body { font-family: "Montserrat", Arial, sans-serif; }
  .spread {
    position: absolute; left: 60px; top: 232px;
    display: flex; gap: 40px;
  }
  .cover {
    position: relative; width: 520px; height: 735px; overflow: hidden;
    box-shadow: 0 12px 30px rgba(0,0,0,.18);
  }
  .cover-art { position: absolute; inset: 0; width: 100%; height: 100%; display: block; }

  .front-logo {
    position: absolute; left: 0; right: 0; top: 250px; text-align: center;
  }
  .brand-name {
    font-weight: 800; color: var(--navy); letter-spacing: .5px; line-height: 1.05;
  }
  .front-logo .brand-name { font-size: 34px; }
  .tagline { font-weight: 600; color: var(--ink); }
  .front-logo .tagline { font-size: 13px; margin-top: 8px; }

  .back-identity { position: absolute; left: 40px; top: 420px; }
  .back-identity .brand-name { font-size: 18px; width: 140px; }
  .back-identity .tagline { font-size: 7.5px; margin-top: 4px; }

  .contact-list { list-style: none; margin-top: 22px; }
  .contact-item {
    display: flex; align-items: center; gap: 9px; margin-bottom: 12px;
    color: var(--white); font-size: 10px; font-weight: 500; line-height: 1.25;
  }
  .contact-icon { width: 14px; height: 14px; flex: none; }
</style>
</head>
<body>
<main class="spread">

  <!-- Back cover -->
  <section class="cover cover-back">
    <svg class="cover-art" viewBox="0 0 520 735" preserveAspectRatio="none" aria-hidden="true">
      <defs>
        <radialGradient id="skyBack" cx="0.75" cy="0.3" r="0.9">
          <stop offset="0" stop-color="var(--sky-mid)"/>
          <stop offset="1" stop-color="var(--sky-deep)"/>
        </radialGradient>
      </defs>
      <rect width="520" height="735" fill="url(#skyBack)"/>
      <path d="M0,300 C140,220 300,170 520,60" stroke="var(--white)" stroke-opacity=".45" stroke-width="6" fill="none"/>
      <path d="M0,340 C160,250 320,210 520,100" stroke="var(--white)" stroke-opacity=".25" stroke-width="14" fill="none"/>
      <path d="M0,620 C160,520 300,420 520,330" stroke="var(--white)" stroke-opacity=".3" stroke-width="4" fill="none"/>
      <path d="M0,676 C180,626 360,548 520,533" stroke="var(--silver)" stroke-width="5" fill="none"/>
      <path d="M0,690 C180,640 360,560 520,545 L520,735 L0,735 Z" fill="var(--navy)"/>
      <path d="M0,690 C180,640 360,560 520,545" stroke="var(--red)" stroke-width="3" fill="none"/>
    </svg>

    <div class="back-identity">
      <div class="brand-name">Crest Contracting</div>
      <div class="tagline">Plumbing • Electrical • Hot Water</div>
      <ul class="contact-list">
        <li class="contact-item">
          <svg class="contact-icon" viewBox="0 0 24 24"><circle cx="12" cy="12" r="12" fill="var(--white)"/><path d="M8 6l2.5 2.5-1.5 2a8 8 0 0 0 4.5 4.5l2-1.5L18 16l-1.5 2C11 18 6 13 6 7.5Z" fill="var(--sky-deep)"/></svg>
          <span>000-9876-543-210<br>000-9876-543-210</span>
        </li>
        <li class="contact-item">
          <svg class="contact-icon" viewBox="0 0 24 24"><circle cx="12" cy="12" r="12" fill="var(--white)"/><path d="M12 5a4.5 4.5 0 0 0-4.5 4.5C7.5 13 12 19 12 19s4.5-6 4.5-9.5A4.5 4.5 0 0 0 12 5Zm0 6.3a1.8 1.8 0 1 1 0-3.6 1.8 1.8 0 0 1 0 3.6Z" fill="var(--sky-deep)"/></svg>
          <span>city name here<br>office address goes here</span>
        </li>
        <li class="contact-item">
          <svg class="contact-icon" viewBox="0 0 24 24"><circle cx="12" cy="12" r="12" fill="var(--white)"/><circle cx="12" cy="12" r="6" fill="none" stroke="var(--sky-deep)" stroke-width="1.6"/><path d="M6 12h12M12 6c-2.5 3-2.5 9 0 12M12 6c2.5 3 2.5 9 0 12" fill="none" stroke="var(--sky-deep)" stroke-width="1.4"/></svg>
          <span>www.websitename.com<br>youremailhere@email.com</span>
        </li>
      </ul>
    </div>
  </section>

  <!-- Front cover -->
  <section class="cover cover-front">
    <svg class="cover-art" viewBox="0 0 520 735" preserveAspectRatio="none">
      <defs>
        <radialGradient id="skyFront" cx="0.5" cy="0.38" r="0.75">
          <stop offset="0" stop-color="var(--sky-pale)"/>
          <stop offset=".55" stop-color="#a9e1f8"/>
          <stop offset="1" stop-color="var(--sky-mid)"/>
        </radialGradient>
      </defs>
      <rect width="520" height="735" fill="url(#skyFront)"/>
      <path d="M0,170 C180,110 330,60 520,10" stroke="var(--white)" stroke-opacity=".5" stroke-width="5" fill="none"/>
      <path d="M0,210 C190,140 340,100 520,50" stroke="var(--white)" stroke-opacity=".25" stroke-width="14" fill="none"/>
      <circle cx="260" cy="285" r="150" fill="none" stroke="#7cc6ea" stroke-opacity=".35" stroke-width="62"
              role="img" aria-label="Ring of line-drawn plumbing and trade icons: tradesman, water heater, pipes, taps, toilet, radiator, washing machine, tools, basin, filters and shower"/>
      <path d="M0,533 C150,518 300,588 520,548" stroke="var(--silver)" stroke-width="5" fill="none"/>
      <path d="M0,545 C150,530 300,600 520,560 L520,735 L0,735 Z" fill="var(--navy)"/>
      <path d="M0,545 C150,530 300,600 520,560" stroke="var(--red)" stroke-width="3" fill="none"/>
    </svg>

    <div class="front-logo">
      <div class="brand-name">Crest Contracting</div>
      <div class="tagline">Plumbing • Electrical • Hot Water</div>
    </div>
  </section>

</main>
</body>
</html>
```